Cafe Business needs a business card design

I already have an ai logo I would like to use and color. I need someone to make a business card for me on adobe illustrator with it. Its for a cafe restaurant opening in Japan I would like to be able to change out the names, contact info, ect on my own from adobe illustrator.

Industry/Entity Type

Business

Contact Information for Business Card

Double sided with logo on one side and info on the other. Name, Tel, fax, email and west

```html
<!DOCTYPE html>
<html lang="en">
<head>
<meta charset="utf-8">
<title>Kumo Bean Cafe – Business Card</title>
<link href="https://fonts.googleapis.com/css2?family=Open+Sans:wght@400;600;700&display=swap" rel="stylesheet">
<style>
  :root {
    --brown: #4a2a14;
    --brown-light: #5e3719;
    --brown-dark: #3a200e;
    --cream: #ece6da;
    --cream-text: #f3eee4;
    --stage: #e6e1d8;
  }
  * { box-sizing: border-box; margin: 0; padding: 0; }
  html, body { width: 1200px; height: 780px; overflow: hidden; }
  body {
    background: var(--stage);
    font-family: "Open Sans", Arial, sans-serif;
    position: relative;
  }
  .card {
    position: absolute;
    top: 240px;
    width: 520px;
    height: 300px;
    border-radius: 3px;
    overflow: hidden;
    box-shadow: 0 6px 18px rgba(40, 25, 10, 0.25);
  }
  .card--front { left: 60px; }
  .card--back {
    left: 620px;
    background: radial-gradient(ellipse at 40% 35%, var(--brown-light), var(--brown) 55%, var(--brown-dark));
  }
  .card__bg { position: absolute; inset: 0; }

  .brand {
    position: absolute;
    display: flex;
    align-items: center;
    gap: 12px;
    font-weight: 700;
    text-transform: uppercase;
    line-height: 1.05;
    letter-spacing: 1px;
  }
  .brand__square { width: 58px; height: 58px; flex: none; }
  .brand__name { font-size: 22px; }
  .brand--front { left: 36px; top: 118px; color: var(--brown); }
  .brand--front .brand__square { background: var(--brown); }
  .brand--back { left: 170px; top: 118px; color: var(--cream-text); }
  .brand--back .brand__square { background: var(--cream); }

  .contact {
    position: absolute;
    left: 318px;
    top: 40px;
    color: var(--cream-text);
  }
  .contact__name { font-size: 20px; font-weight: 700; line-height: 1.1; }
  .contact__role { font-size: 12px; margin-bottom: 22px; }
  .contact__address { font-size: 12px; line-height: 1.45; margin-bottom: 14px; }
  .contact__list { list-style: none; font-size: 12px; line-height: 1.3; }
  .contact__list li { display: flex; align-items: center; gap: 7px; margin-bottom: 3px; }
  .contact__icon { width: 13px; height: 13px; flex: none; }
  .contact__web { font-size: 12px; margin-top: 10px; }
</style>
</head>
<body>

<section class="card card--front">
  <svg class="card__bg" viewBox="0 0 520 300" width="520" height="300" aria-hidden="true">
    <rect width="520" height="300" fill="var(--cream)"/>
    <path d="M200 0 C290 70 250 210 340 300 L520 300 L520 0 Z" fill="var(--brown)"/>
    <path d="M214 0 C302 70 264 210 354 300" fill="none" stroke="var(--cream)" stroke-width="2"/>
  </svg>

  <div class="brand brand--front">
    <span class="brand__square"></span>
    <span class="brand__name">Kumo Bean<br>Cafe</span>
  </div>

  <div class="contact">
    <p class="contact__name">Employee Name</p>
    <p class="contact__role">Director</p>
    <p class="contact__address">P.O. Box 000, 2nd Street<br>Maple Hill, USA</p>
    <ul class="contact__list">
      <li>
        <svg class="contact__icon" viewBox="0 0 13 13"><rect width="13" height="13" fill="var(--cream)"/><path d="M3.5 3 L5.3 3 L6 5 L5 5.8 C5.6 7 6.2 7.6 7.2 8.1 L8 7.1 L10 7.8 L10 9.6 C6 9.8 3.2 7 3.5 3 Z" fill="var(--brown)"/></svg>
        0123 456 789
      </li>
      <li>
        <svg class="contact__icon" viewBox="0 0 13 13"><rect width="13" height="13" fill="var(--cream)"/><rect x="3" y="5" width="7" height="5" fill="var(--brown)"/><rect x="4.5" y="2.5" width="4" height="3" fill="none" stroke="var(--brown)"/></svg>
        0123 456 789
      </li>
      <li>
        <svg class="contact__icon" viewBox="0 0 13 13"><rect width="13" height="13" fill="var(--cream)"/><rect x="2.5" y="4" width="8" height="5.5" fill="none" stroke="var(--brown)"/><path d="M2.5 4 L6.5 7 L10.5 4" fill="none" stroke="var(--brown)"/></svg>
        hello@kumobean.jp
      </li>
    </ul>
    <p class="contact__web">www.kumobean.jp</p>
  </div>
</section>

<section class="card card--back">
  <div class="brand brand--back">
    <span class="brand__square"></span>
    <span class="brand__name">Kumo Bean<br>Cafe</span>
  </div>
</section>

</body>
</html>
```